Real Estate Marketing Company Needs 1 Page 8.5x11 Price List Flyer Design

We need a 1 page 8.5in x 11in price list flyer that is intended for drop off at local offices. This is intended to show all the services we offer including pricing to potential new clients. It should be separated into sections for the different services we offer. I'd also like some photos and our Logo on the list to make it look nice so its not all text. Try to incorporate the logo colors in the design.

Industry/Entity Type

Real Estate

Requirements
Must have
• Price List
• Photos
• Logo
• website address

```html
<!DOCTYPE html>
<html lang="en">
<head>
<meta charset="utf-8">
<title>Keystone Lens – Price List</title>
<link rel="stylesheet" href="https://fonts.googleapis.com/css2?family=Cinzel:wght@600&family=Arimo:wght@400;700&family=Tinos&display=swap">
<style>
  :root{
    --page:#ffffff;
    --canvas:#ffffff;
    --ink:#333333;
    --black:#111111;
    --charcoal:#333333;
    --red:#a51d24;
    --sage:#c9dc8a;
    --sky:#a8e3e8;
    --peach:#f3d29c;
    --cloud-blue:#a8dcec;
    --cloud-peach:#f4cf98;
    --cloud-lime:#8dc63f;
    --cloud-green:#1a9e4a;
    --cloud-orange:#f0a24a;
  }
  *{box-sizing:border-box;margin:0;padding:0}
  html,body{width:1200px;height:1000px;overflow:hidden;background:var(--canvas)}
  body{position:relative;font-family:"Arimo",Arial,sans-serif;color:var(--ink)}
  .flyer{position:absolute;left:234px;top:26px;width:732px;height:947px;background:var(--page);border-left:1px solid #e4e4e4;border-right:1px solid #e4e4e4}
  .band{position:absolute;left:234px;width:732px}
  .band--dark-top{top:26px;height:10px;background:var(--charcoal)}
  .band--red-top{top:40px;height:8px;background:var(--red)}
  .band--red-bottom{top:950px;height:8px;background:var(--red)}
  .band--dark-bottom{top:962px;height:11px;background:var(--charcoal)}

  .brand{position:absolute;left:290px;top:58px;width:240px;text-align:center}
  .brand__dot{display:block;width:94px;height:94px;margin:0 auto 14px;border-radius:50%;background:var(--black)}
  .brand__name{font-family:"Cinzel",serif;font-weight:600;font-size:31px;color:var(--black);letter-spacing:.5px;white-space:nowrap}

  .cloud span{position:absolute;font-family:"Tinos","Times New Roman",serif;white-space:nowrap;line-height:1}
  .c-blue{color:var(--cloud-blue)} .c-peach{color:var(--cloud-peach)} .c-lime{color:var(--cloud-lime)}
  .c-green{color:var(--cloud-green)} .c-orange{color:var(--cloud-orange)}

  .photo{position:absolute}
  .photo polygon.frame{fill:none;stroke-width:3.6}

  .tag{position:absolute;background:var(--red);color:#fff;font-weight:700;font-size:12.5px;padding:0 7px;height:23px;line-height:23px;white-space:nowrap}
  .list{position:absolute;font-size:12.5px;line-height:14px;color:var(--ink)}
  .row{display:flex;white-space:nowrap}
  .row__label{flex:none}
  .pricing .row__label{width:107px}
  .extras .row__label{width:104px}

  .contact{position:absolute;left:234px;width:732px;top:924px;text-align:center;font-size:12.5px;color:var(--ink)}
</style>
</head>
<body>
  <div class="flyer"></div>
  <div class="band band--dark-top"></div>
  <div class="band band--red-top"></div>

  <header class="brand">
    <span class="brand__dot"></span>
    <div class="brand__name">Keystone Lens</div>
  </header>

  <div class="cloud" aria-label="Services">
    <span class="c-blue" style="left:545px;top:62px;font-size:14px">AERIAL VIDEO</span>
    <span class="c-peach" style="left:647px;top:59px;font-size:18px">BRANDED VIDEO TOUR</span>
    <span class="c-lime" style="left:560px;top:73px;font-size:27px">AERIAL PHOTOS</span>
    <span class="c-peach" style="left:768px;top:75px;font-size:11px">AERIAL PHOTOS</span>
    <span class="c-green" style="left:533px;top:98px;font-size:11px">TWILIGHT PHOTOS</span>
    <span class="c-blue" style="left:634px;top:98px;font-size:20px">AERIAL VIDEO</span>
    <span class="c-orange" style="left:774px;top:96px;font-size:8px">BRANDED VIDEO TOUR</span>
    <span class="c-lime" style="left:778px;top:104px;font-size:13px">AERIAL PHOTOS</span>
    <span class="c-peach" style="left:534px;top:116px;font-size:12px">AERIAL PHOTOS</span>
    <span class="c-green" style="left:637px;top:117px;font-size:20px">TWILIGHT PHOTOS</span>
    <span class="c-lime" style="left:602px;top:137px;font-size:11px">AERIAL PHOTOS</span>
  </div>

  <!-- pool garden -->
  <svg class="photo" style="left:243px;top:213px;width:254px;height:254px" viewBox="-100 -100 200 200">
    <defs><linearGradient id="g-pool" x1="0" y1="0" x2="0" y2="1"><stop offset="0" stop-color="#5e8a4a"/><stop offset=".6" stop-color="#3f7bb0"/><stop offset="1" stop-color="#8a7a5a"/></linearGradient></defs>
    <polygon class="frame" stroke="var(--sage)" points="96,0 77.7,56.4 29.7,91.3 -29.7,91.3 -77.7,56.4 -96,0 -77.7,-56.4 -29.7,-91.3 29.7,-91.3 77.7,-56.4"/>
    <polygon role="img" aria-label="Photo of a landscaped backyard pool with a pool house" fill="url(#g-pool)" points="84,0 68,49.4 26,79.9 -26,79.9 -68,49.4 -84,0 -68,-49.4 -26,-79.9 26,-79.9 68,-49.4"/>
  </svg>

  <!-- living room -->
  <svg class="photo" style="left:467px;top:322px;width:236px;height:236px" viewBox="-100 -100 200 200">
    <defs><linearGradient id="g-room" x1="0" y1="0" x2="0" y2="1"><stop offset="0" stop-color="#d8c9a8"/><stop offset=".5" stop-color="#a9825a"/><stop offset="1" stop-color="#7a5a3c"/></linearGradient></defs>
    <polygon class="frame" stroke="var(--sky)" points="96,0 77.7,56.4 29.7,91.3 -29.7,91.3 -77.7,56.4 -96,0 -77.7,-56.4 -29.7,-91.3 29.7,-91.3 77.7,-56.4"/>
    <polygon role="img" aria-label="Photo of a living room with fireplace and chandelier" fill="url(#g-room)" points="84,0 68,49.4 26,79.9 -26,79.9 -68,49.4 -84,0 -68,-49.4 -26,-79.9 26,-79.9 68,-49.4"/>
  </svg>

  <!-- porch -->
  <svg class="photo" style="left:653px;top:141px;width:294px;height:294px" viewBox="-100 -100 200 200">
    <defs><linearGradient id="g-porch" x1="0" y1="0" x2="0" y2="1"><stop offset="0" stop-color="#7fb44a"/><stop offset=".5" stop-color="#d9d2c4"/><stop offset="1" stop-color="#9a9690"/></linearGradient></defs>
    <polygon class="frame" stroke="var(--peach)" points="96,0 77.7,56.4 29.7,91.3 -29.7,91.3 -77.7,56.4 -96,0 -77.7,-56.4 -29.7,-91.3 29.7,-91.3 77.7,-56.4"/>
    <polygon role="img" aria-label="Photo of a covered porch with a swing bench and orange cushions" fill="url(#g-porch)" points="84,0 68,49.4 26,79.9 -26,79.9 -68,49.4 -84,0 -68,-49.4 -26,-79.9 26,-79.9 68,-49.4"/>
  </svg>

  <!-- aerial house -->
  <svg class="photo" style="left:673px;top:457px;width:284px;height:284px" viewBox="-100 -100 200 200">
    <defs><linearGradient id="g-aerial" x1="0" y1="0" x2="0" y2="1"><stop offset="0" stop-color="#8fa6a8"/><stop offset=".15" stop-color="#3d6a2a"/><stop offset="1" stop-color="#2f5a22"/></linearGradient></defs>
    <polygon class="frame" stroke="var(--sage)" points="96,0 77.7,56.4 29.7,91.3 -29.7,91.3 -77.7,56.4 -96,0 -77.7,-56.4 -29.7,-91.3 29.7,-91.3 77.7,-56.4"/>
    <polygon role="img" aria-label="Aerial photo of a large house surrounded by forest" fill="url(#g-aerial)" points="84,0 68,49.4 26,79.9 -26,79.9 -68,49.4 -84,0 -68,-49.4 -26,-79.9 26,-79.9 68,-49.4"/>
  </svg>

  <!-- lake -->
  <svg class="photo" style="left:234px;top:627px;width:298px;height:298px" viewBox="-100 -100 200 200">
    <defs><linearGradient id="g-lake" x1="0" y1="0" x2="0" y2="1"><stop offset="0" stop-color="#4a7fc0"/><stop offset=".35" stop-color="#c9d6e4"/><stop offset=".55" stop-color="#6d8a6a"/><stop offset="1" stop-color="#b07a2c"/></linearGradient></defs>
    <polygon class="frame" stroke="var(--peach)" points="96,0 77.7,56.4 29.7,91.3 -29.7,91.3 -77.7,56.4 -96,0 -77.7,-56.4 -29.7,-91.3 29.7,-91.3 77.7,-56.4"/>
    <polygon role="img" aria-label="Aerial photo of a lake among autumn forest hills" fill="url(#g-lake)" points="84,0 68,49.4 26,79.9 -26,79.9 -68,49.4 -84,0 -68,-49.4 -26,-79.9 26,-79.9 68,-49.4"/>
  </svg>

  <div class="tag" style="left:259px;top:531px">Package Pricing:</div>
  <div class="list pricing" style="left:265px;top:563px">
    <div class="row"><span class="row__label">Silver Package:</span><span>15 Photos + Floor Plan (3,500 sqft) - $225</span></div>
    <div class="row"><span class="row__label">Gold Package:</span><span>25 Photos + Floor Plan (4,500 sqft) - $300</span></div>
    <div class="row"><span class="row__label">Platinum Package:</span><span>35 Photos + Floor Plan (5,500 sqft) - $375</span></div>
  </div>

  <div class="tag" style="left:522px;top:637px">PHOTOGRAPHY ONLY</div>
  <div class="list" style="left:527px;top:669px">
    <div>15 Photo Bundle: $100</div>
    <div>25 Photo Bundle: $150</div>
    <div>35 Photo Bundle: $200</div>
  </div>

  <div class="tag" style="left:522px;top:744px">ADDITIONAL SERVICES</div>
  <div class="list extras" style="left:529px;top:776px">
    <div class="row"><span class="row__label">Aerial Photos:</span><span>3-6 Photos - $200 ($75 if combined with another package)</span></div>
    <div class="row"><span class="row__label">Aerial Video:</span><span>(1-3 min video) - $375</span></div>
    <div class="row"><span class="row__label">Twilight Photos:</span><span>3-6 Photos - $225</span></div>
    <div class="row"><span class="row__label">Luxury Package:</span><span>$2,000 (includes all services listed)</span></div>
    <div>Branded Video Tour w/ Aerial Video: (2-4 min video of property) - $800-$1300</div>
    <div>(voiceover optional, call for details)</div>
  </div>

  <p class="contact">For more information or to book a shoot please visit our website: www.KeystoneLensStudio.com or call Mason at 555-014-2287</p>

  <div class="band band--red-bottom"></div>
  <div class="band band--dark-bottom"></div>
</body>
</html>
```